China Restaurant sucht kreatives Speisekarten-Design
Zielgruppe
Wir sind ein China Restaurant und sind auf der Suche nach der perfekten Speisekarte. Unsere Zielgruppe sind Familien sowie ältere Kundschaften.
Aufgabenstellung
Die Speisekarte soll in einem Asiatischen Stil designt werden, der Designer kann seine Kreativität frei lauf lassen. Wir benötigen DIN 4 Format.

```html
<!DOCTYPE html>
<html lang="de">
<head>
<meta charset="utf-8">
<title>Getränke</title>
<link rel="stylesheet" href="https://fonts.googleapis.com/css2?family=Catamaran:wght@400;500&family=Courgette&display=swap">
<style>
  :root {
    --paper-cream: #f8efd6;
    --paper-white: #ffffff;
    --ink: #1e1a16;
    --band-red: #6e1912;
    --panel-red: #7a1a12;
    --gold: #d8b46a;
  }
  * { margin: 0; padding: 0; box-sizing: border-box; }
  html, body { width: 848px; height: 1200px; overflow: hidden; }
  body { font-family: "Catamaran", sans-serif; color: var(--ink); }

  .menu-page {
    position: relative;
    width: 848px;
    height: 1200px;
    background: var(--paper-white);
    overflow: hidden;
  }
  .paper-pattern {
    position: absolute;
    left: 0; top: 0;
    width: 609px; height: 1200px;
    background: linear-gradient(165deg, var(--paper-cream) 0%, #fbf4e3 45%, var(--paper-white) 75%);
  }
  .side-band {
    position: absolute;
    left: 609px; top: 0;
    width: 239px; height: 1200px;
    background: var(--band-red);
  }
  .side-title {
    position: absolute;
    left: 737px; top: 427px;
    transform: translate(-50%, -50%) rotate(-90deg);
    font-family: "Courgette", cursive;
    font-size: 46px;
    font-weight: 400;
    color: var(--gold);
    text-shadow: 2px 3px 3px rgba(0,0,0,0.55);
    white-space: nowrap;
  }
  .dragon-panel {
    position: absolute;
    left: 609px; top: 785px;
    width: 239px; height: 345px;
    background: radial-gradient(ellipse at 55% 50%, #8a2a1a 0%, var(--panel-red) 70%);
  }

  .drinks-section { position: absolute; left: 66px; width: 440px; }
  .section-title {
    position: absolute;
    left: 0;
    font-family: "Courgette", cursive;
    font-size: 21px;
    font-weight: 400;
    line-height: 28px;
    white-space: nowrap;
  }
  .price-list { position: absolute; left: 0; width: 440px; }
  .price-row {
    display: grid;
    grid-template-columns: 320px 70px 42px;
    font-size: 16px;
    line-height: 20.6px;
    height: 20.6px;
    white-space: nowrap;
  }
  .price-row .size, .price-row .price-large { text-align: right; }
  .price-row .price-small, .price-row .size-small { text-align: left; }
  .group-label { font-size: 16px; line-height: 20.6px; height: 20.6px; }
  .spacer { height: 20.6px; }
</style>
</head>
<body>
<main class="menu-page">
  <div class="paper-pattern"></div>
  <div class="side-band"></div>
  <div class="side-title">Getränke</div>
  <div class="dragon-panel" role="img" aria-label="Goldene Illustration eines chinesischen Drachen zwischen Wolken"></div>

  <section class="drinks-section" style="top:0">
    <h2 class="section-title" style="top:76px">Alkoholfreie&nbsp; Getränke</h2>
    <div class="price-list" style="top:101px">
      <div class="price-row"><span></span><span class="size-small">klein</span><span class="size">groß</span></div>
      <div class="price-row"><span>Cola/ Orangenlimo/ Kräuterlimo</span><span class="price-small">2,10</span><span class="price-large">3,40</span></div>
      <div class="price-row"><span>Cola-Orange</span><span class="price-small">2,20</span><span class="price-large">3,50</span></div>
      <div class="price-row"><span>Eistee</span><span class="price-small">2,10</span><span class="price-large">3,00</span></div>
      <div class="price-row"><span>Soda</span><span class="price-small">1,80</span><span class="price-large">2,50</span></div>
      <div class="price-row"><span>Mineralwasser mit/ohne</span><span class="price-small">2,10</span><span></span></div>
      <div class="price-row"><span>Apfel-, Orangen-, Johannisbeersaft</span><span class="price-small">2,20</span><span class="price-large">3,60</span></div>
      <div class="price-row"><span>Bitter Lemon</span><span class="price-small">2,30</span><span class="price-large">3,60</span></div>
      <div class="price-row"><span>Mangosaft/ Lycheesaft</span><span class="price-small">2,50</span><span></span></div>
    </div>

    <h2 class="section-title" style="top:331px">Flaschenweine</h2>
    <div class="price-list" style="top:378px">
      <div class="group-label">Weiß</div>
      <div class="price-row"><span>Grüner Veltliner</span><span class="price-small">14,50</span><span></span></div>
      <div class="price-row"><span>Welschriesling</span><span class="price-small">14,50</span><span></span></div>
      <div class="spacer"></div>
      <div class="group-label">Rot</div>
      <div class="price-row"><span>Beaujolais</span><span class="price-small">19,40</span><span></span></div>
      <div class="price-row"><span>Blaufränkisch</span><span class="price-small">14,50</span><span></span></div>
    </div>

    <h2 class="section-title" style="top:563px">Alkoholische Getränke</h2>
    <div class="price-list" style="top:590px">
      <div class="price-row"><span></span><span class="size-small">klein</span><span class="size">groß</span></div>
      <div class="price-row"><span>Lindenbier vom Fass</span><span class="price-small">3,00</span><span class="price-large">3,60</span></div>
      <div class="price-row"><span>Radler</span><span class="price-small">3,20</span><span class="price-large">3,80</span></div>
      <div class="price-row"><span>Chinesisches Bier</span><span class="price-small">3,60</span><span></span></div>
      <div class="price-row"><span>Weißbier hell/ dunkel</span><span class="price-small">3,60</span><span></span></div>
      <div class="price-row"><span>alkoholfreies Bier</span><span class="price-small">3.60</span><span></span></div>
    </div>

    <h2 class="section-title" style="top:755px">offene Weine</h2>
    <div class="price-list" style="top:781px">
      <div class="price-row"><span></span><span class="size-small">1/8</span><span class="size">1/4</span></div>
      <div class="price-row"><span>Weißwein</span><span class="price-small">2,10</span><span class="price-large">3,00</span></div>
      <div class="price-row"><span>Rotwein</span><span class="price-small">2.10</span><span class="price-large">3,00</span></div>
      <div class="price-row"><span>weißer Spritzer</span><span class="price-small">2,50</span><span></span></div>
      <div class="price-row"><span>süßer Spritzer</span><span class="price-small">2,70</span><span></span></div>
      <div class="price-row"><span>roter Spritzer</span><span class="price-small">2,50</span><span></span></div>
      <div class="price-row"><span>süßer roter Spritzer</span><span class="price-small">2,80</span><span></span></div>
      <div class="price-row"><span>Lambrusco</span><span class="price-small">2,30</span><span class="price-large">3,90</span></div>
      <div class="price-row"><span>Rosewein</span><span class="price-small">2,10</span><span class="price-large">3,00</span></div>
    </div>
  </section>
</main>
</body>
</html>
```